Gestaltung eines Merkblattes
Ein Entwurf, der genau meinen Vorstellungen entspricht. Eine Abwicklung, die schneller und professioneller nicht sein könnte. Die Kommunikation - sehr symphatisch und kundenorientiert. Resumee: Besser geht es nicht.
Zielgruppe
www.tierklang-analytik.de/ Medizinische Bioresonanzanalysen für Pferde. Die Kundschaft besteht hauptsächlich aus Frauen, Alter von 20- 55 Jahre.
Bei dem Projekt handelt es sich um die Gestaltung eines wichtigen Merkblattes, das jedem Kunde zusammen mit dem Befund der Analyse gemailt wird. Es enthält wichtige Informationen rund um die Bioresonanzanalyse und sollte als pdf- Datei vorliegen.
Aufgabenstellung
Kernproblem: Die Kunden lesen das Merkblatt gar nicht oder nicht sorgfältig. So entstehen viele Fragen in der Folge, die nicht notwendig wären.
Wir benötigen eine pdf- Datei, die zum Lesen anregt, gerne gelesen wird und in der die wichtigsten Aspekte in das Auge fallen. Diese wurden von mir in der Worddatei, die den Text enthält, rot markiert.
Der Text in schwarz ist deutlich weniger wichtig.
Ach ja, die Überschrift ist doof. 'Allgemeine Hinweise' das animiert nicht wirklich zum Lesen. Falls Sie eine griffige Idee haben, sehr gerne.

```html
<!DOCTYPE html>
<html lang="de">
<head>
<meta charset="utf-8">
<title>Wissenswerte Hinweise – Merkblatt</title>
<link href="https://fonts.googleapis.com/css2?family=Ubuntu:wght@400;500&family=Hind:wght@400;500&display=swap" rel="stylesheet">
<style>
  :root{
    --green:#b7c16b;
    --green-soft:#bcc573;
    --ink:#1f1f1f;
    --paper:#ffffff;
  }
  *{box-sizing:border-box;margin:0;padding:0}
  html,body{width:1200px;height:1200px;overflow:hidden}
  body{background:var(--green-soft);position:relative;font-family:"Hind",Arial,sans-serif;color:var(--ink)}
  .sheet{position:absolute;top:254px;width:489px;height:692px;background:var(--paper);box-shadow:0 2px 10px rgba(0,0,0,.18)}
  .sheet--one{left:79px}
  .sheet--two{left:632px}
  .title{position:absolute;left:32px;top:28px;font-family:"Ubuntu",sans-serif;font-weight:400;font-size:37px;line-height:36px;color:var(--green);letter-spacing:.3px}
  .title span{display:block}
  .title .indent{padding-left:36px}
  .brand{position:absolute;left:338px;top:62px;display:flex;align-items:center;gap:6px;font-family:"Ubuntu",sans-serif;font-weight:500;font-size:12px;color:var(--green)}
  .brand i{display:block;width:12px;height:12px;border-radius:50%;background:var(--green)}
  .bar{position:absolute;left:24px;width:440px;height:22px;border:1px solid var(--green);display:flex;align-items:stretch}
  .sheet--two .bar{left:25px;width:439px}
  .bar h2{background:var(--green);color:#fff;font-family:"Ubuntu",sans-serif;font-weight:400;font-size:12.5px;line-height:21px;padding:0 8px;white-space:nowrap}
  .bar .note{flex:1;text-align:right;color:var(--green);font-size:8.2px;line-height:21px;padding-right:8px}
  .bar .mark{margin-left:auto;width:22px;background:var(--green);color:#fff;font-family:"Ubuntu",sans-serif;font-weight:500;font-size:11px;line-height:21px;text-align:center}
  .bar .note + .mark{margin-left:0}
  .text{position:absolute;left:32px;width:425px;font-size:8.1px;line-height:12.9px}
  .text p + p{margin-top:6px}
  .cols{position:absolute;left:32px;width:430px;display:grid;grid-template-columns:208px 208px;column-gap:16px;font-size:8.1px;line-height:12.9px}
  .cols p + p{margin-top:6px}
  .page-no{position:absolute;right:33px;top:654px;font-size:6px;color:var(--green)}
</style>
</head>
<body>

<section class="sheet sheet--one">
  <h1 class="title"><span>Wissenswerte</span><span class="indent">Hinweise</span></h1>
  <div class="brand"><i></i>Tierklang-Analytik</div>

  <div class="bar" style="top:126px"><h2>Das wichtigste zuerst</h2><span class="note">Das sollten Sie umbedingt wissen!</span><span class="mark">!</span></div>
  <div class="text" style="top:157px">
    <p>Die empfohlenen Präparate können (wenn nicht anders angegeben) in das normale Kraftfutter gegeben werden. Tropfen und Bachblüten bitte auf ein kleines Stück trockenes Brot, Zwieback, bei Pferden, die kein Getreide fressen dürfen, auf ein Stück Reiswaffel geben, und dem Pferd direkt füttern.</p>
  </div>
  <div class="cols" style="top:209px">
    <div>
      <p>Mineralbase Pulver muss nicht, wie vom Hersteller angegeben, in Wasser aufgelöst werden. Eine Gabe in das Kraftfutter, Heucobs etc. vermindert nicht die Wirkung.</p>
      <p>Bitte füttern Sie alle Präparate, außer es sind abweichende Empfehlungen vorhanden, ohne Unterbrechung, bis Ihnen das Ergebnis der ersten Nachtestung vorliegt. Pausen von mehr als zwei Tagen können zu Beginn der Behandlung die positive Entwicklung Ihres Pferdes beeinträchtigen.</p>
    </div>
    <div>
      <p>Falls Ihr Pferd sehr wählerisch ist bei der Zufütterung von Präparaten in Pellets- oder Pulverform, dann beginnen Sie mit einer sehr kleinen Dosierung von z. B. ½ Teelöffel und steigern diese sehr langsam. Bei trockenem Futter (Müsli, Hafer) sortieren manche Pferde gerne aus. Hier ist es sinnvoll, das Futter anzufeuchten, etwas Heucobs oder getreidefreies Mash dazuzugeben.</p>
    </div>
  </div>

  <div class="bar" style="top:364px"><h2>Nachtestung</h2><span class="mark">!</span></div>
  <div class="cols" style="top:395px">
    <div><p>Wir bestätigen den Eingang der Probe zur Nachtestung nicht. In regelmäßigen Abständen werden alle Befunde nachgetestet. Wir senden Ihnen im Anschluss per Mail das neue Ergebnis mit einer aktualisierten Therapieempfehlung zu.</p></div>
    <div><p>Wir brauchen für die Nachtestung eine neue Haarprobe und ein kurzes Feedback zu der aktuellen Entwicklung Ihres Pferdes. Mehr nicht.</p></div>
  </div>

  <div class="bar" style="top:480px"><h2>Bachblüten</h2><span class="mark">!</span></div>
  <div class="cols" style="top:511px">
    <div><p>Wenn die Therapieempfehlung eine Übersicht an Bachblüten enthält, dann spiegeln diese den seelischen Zustand Ihres Pferdes wieder, der von seinen aktuellen Lebensbedingungen, seiner körperlichen Belastung durch Krankheit und durch Abläufe in seiner Herde beeinflusst wird. Erfahrungsgemäß bezieht sich die Darstellung der Blüten bei Pferden, die in einer Herde leben, häufig mehr auf die Gefühle des Pferdes gegenüber seinen Artgenossen als auf den Kontakt mit dem Menschen.</p></div>
    <div><p>Die meisten Apotheken kennen sich aus mit der Herstellung einer Bachblütenmischung. Falls nicht, hier die Anleitung: in ein 30 ml Medizinfläschchen mit Tropfvorrichtung oder Pipette gibt man 10 ml Alkohol (Brandy oder Weinbrand), 20 ml Quellwasser oder stilles Mineralwasser (ohne Kohlensäure; kein destilliertes Wasser!) und 2-3 Tropfen von jeder Blüte, die im Moment benötigt wird. Als Alternative zu Alkohol kann auch Obstessig eingesetzt werden.</p></div>
  </div>
  <span class="page-no">Seite 1/2</span>
</section>

<section class="sheet sheet--two">
  <div class="bar" style="top:33px"><h2>Tierarzt</h2></div>
  <div class="text" style="top:64px;width:430px">
    <p>Wir weisen ausdrücklich darauf hin, dass die Ergebnisse der Bioresonanzanalyse nicht kompatibel sind mit den herkömmlichen Labormethoden und anderen tierärztlichen Diagnoseformen.</p>
  </div>
  <div class="cols" style="top:102px">
    <div>
      <p>Ein Beispiel: Wenn wir eine Belastung der Leber mit dem Leberegel Fasciola hepatica feststellen, kann eine klassische Laboruntersuchung zu dem gleichen Thema ergebnislos bleiben. Der Grund hierfür liegt u.a. in der sehr unterschiedlichen Beurteilung und Herangehensweise.</p>
      <p>Das Wohl Ihres Pferdes steht jederzeit im Mittelpunkt. Falls in der Zeit der Umsetzung der Therapie-empfehlung bei Ihrem Pferd Symptome auftreten, die eine tierärztliche und schnelle Hilfe</p>
    </div>
    <div>
      <p>dringend erforderlich machen, zögern Sie bitte nie, den Tierarzt zu rufen.</p>
      <p>Bitte informieren Sie mich vorab, wenn Ihr Pferd zum Zeitpunkt der Nachtestung Medikamente von dem Tierarzt erhält. Relevant sind Antibiotika, Cortison, sowie andere, massiv entzündungshemmende Präparate. In diesem Fall sprechen wir miteinander ab, ob die Nachtestung verschoben wird. Wurmkuren und Impfungen sind für die Durchführung der Nachtestung nicht von Bedeutung.</p>
    </div>
  </div>

  <div class="bar" style="top:257px"><h2>Impfung</h2></div>
  <div class="text" style="top:288px;width:430px">
    <p>Wir geben generell keine Impfempfehlungen. Es hat sich jedoch in den vergangenen Jahren gezeigt, dass es sinnvoll ist, Impfungen (besonders Influenza- und Herpes- Impfungen) vor Beginn der Umsetzung der Therapieempfehlung einzuplanen. Werden sie zu einem späteren Zeitpunkt vorgenommen, kann es zu Rückschritten in der ansonsten positiven Entwicklung kommen.</p>
  </div>

  <div class="bar" style="top:361px"><h2>Doping</h2></div>
  <div class="cols" style="top:392px">
    <div>
      <p>Zum Schutz der Pferde bestehen Anti- Doping Richtlinien, die klare Regeln vorgeben, welche Zu-satzfutterpräparate, Medikamente und auch Naturheilmittel einem Turnierpferd vor und während einem Start in einer Turnierprüfung gefüttert werden dürfen. Die Einhaltung der Vorgaben wird durch stichpunktartige Kontrollen überprüft.</p>
      <p>Bitte beachten Sie die Anti- Doping Richtlinien der RSV und weiterer Pferdesportverbände und halten Sie bei</p>
    </div>
    <div>
      <p>der Fütterung aller Präparate unserer Therapie-empfehlung eine Karenzzeit von 48 Stunden vor Prüfungsbeginn ein, wenn Sie mit Ihrem Pferd an einem Wettbewerb teilnehmen. Ausnahme! Bei der Zufütterung von Präparaten, die Teufelskralle enthalten, besteht eine Karenzzeit von 4 Tagen.</p>
      <p>Wir übernehmen für die Folgen einer Nichtbeachtung der nationalen oder internationalen Anti- Doping-richtlinien keine Haftung.</p>
    </div>
  </div>

  <div class="bar" style="top:535px"><h2>Tragende Stuten/ Stuten mit Fohlen bei Fuß</h2></div>
  <div class="cols" style="top:566px">
    <div><p>Wir übernehmen keine Haftung für die Gabe der von uns empfohlenen Naturheilmittel bei tragenden Stute und Stuten mit Fohlen bei Fuß. Jedes der angegebenen Mittel wurde von mir mit großer Sorgfalt ausgewählt. Die aktuell vorhandenen,</p></div>
    <div><p>medizinischen Studien zu der Wirkung von Naturheilmitteln bei tragenden Stuten sind jedoch nicht umfangreich genug, um Nebenwirkungen vollständig ausschließen zu können.</p></div>
  </div>
  <span class="page-no">Seite 2/2</span>
</section>

</body>
</html>
```